Workbook Cover Design

I am needing the cover for a workbook designed. I have attached a sample cover along with a few images giving an idea what at I am looking for. I'm open to new color schemes. I also attached a flyer of the event to give you an idea of the current color theme. The workbook will be approximately 8.5 x 11.

Title : Fellowship Workshop 202
Lorna Tebbit Ministries

On the cover I would like to have four sections with the following title under each section:
Evangelism (use photo similar to hands with cross)
Praying in Tongues (Photo similar to bird with heart or one with a mouth speaking)
Authority of the Believer (Photo with badge or similar)
Healing (Photo of man and wheelchair or similar)

Using silhouettes are okay, but I prefer not to have any actual faces of people.

```html
<!DOCTYPE html>
<html lang="en">
<head>
<meta charset="utf-8">
<title>Fellowship Workshop 202 – Workbook Cover</title>
<link href="https://fonts.googleapis.com/css2?family=Great+Vibes&family=Oswald:wght@500&family=Montserrat:wght@500;600&family=Open+Sans:wght@700&display=swap" rel="stylesheet">
<style>
  :root {
    --backdrop: #d9d9d9;
    --cover-brown: #561708;
    --deep-brown: #3a0d03;
    --tan: #c4955f;
    --gold-text: #eec48a;
    --white: #ffffff;
    --line: #d9aa6e;
  }
  html, body {
    margin: 0;
    width: 1116px;
    height: 1200px;
    overflow: hidden;
    background: var(--backdrop);
  }
  .cover {
    position: absolute;
    left: 111px;
    top: 30px;
    width: 894px;
    height: 1140px;
    background: var(--cover-brown);
    overflow: hidden;
  }
  .cover-lines {
    position: absolute;
    inset: 0;
  }
  .ministry-mark {
    position: absolute;
    left: 470px;
    transform: translateX(-50%);
    white-space: nowrap;
    color: var(--gold-text);
    font-family: "Montserrat", sans-serif;
    font-weight: 500;
  }
  .mark-initials { top: 40px; font-size: 42px; letter-spacing: 6px; }
  .mark-name {
    top: 98px;
    font-size: 19px;
    letter-spacing: 3px;
    background: var(--cover-brown);
    padding: 0 14px;
  }
  .title-block {
    position: absolute;
    left: 100px;
    top: 150px;
    width: 339px;
    height: 354px;
    background: var(--tan);
  }
  .split {
    position: absolute;
    left: 100px;
    width: 742px;
    text-align: center;
    white-space: nowrap;
  }
  .split.on-tan { color: var(--deep-brown); clip-path: inset(-40px 403px -40px 0); }
  .split.on-brown { color: var(--gold-text); clip-path: inset(-40px 0 -40px 339px); }
  .title-script {
    top: 160px;
    font-family: "Great Vibes", cursive;
    font-size: 92px;
    line-height: 1;
  }
  .title-main {
    position: absolute;
    left: 100px;
    width: 742px;
    top: 238px;
    text-align: center;
    font-family: "Oswald", sans-serif;
    font-weight: 500;
    font-size: 98px;
    line-height: 1;
    color: var(--white);
    letter-spacing: 1px;
    white-space: nowrap;
  }
  .tagline {
    top: 356px;
    font-family: "Montserrat", sans-serif;
    font-weight: 500;
    font-size: 25px;
    line-height: 33px;
    letter-spacing: 1px;
  }
  .sessions {
    top: 436px;
    font-family: "Montserrat", sans-serif;
    font-weight: 500;
    font-size: 46px;
    letter-spacing: 9px;
  }
  .session-strip {
    position: absolute;
    left: 803px;
    top: 504px;
    width: 39px;
    height: 469px;
    background: var(--tan);
  }
  .session-grid {
    position: absolute;
    left: 100px;
    top: 511px;
    width: 703px;
    height: 462px;
    display: grid;
    grid-template-columns: 1fr 1fr;
    grid-template-rows: 1fr 1fr;
  }
  .session { position: relative; }
  .session-label {
    position: absolute;
    bottom: 10px;
    font-family: "Open Sans", sans-serif;
    font-weight: 700;
    font-size: 20px;
    color: var(--white);
    letter-spacing: 0.5px;
    white-space: nowrap;
  }
  .label-left { left: 8px; }
  .label-right { right: 12px; }
  .evangelism { background: radial-gradient(circle at 50% 55%, #fff6d8 0%, #d9b88a 30%, #8e7864 70%, #5f5a5e 100%); }
  .tongues { background: radial-gradient(circle at 45% 50%, #ff9a2e 0%, #b8400c 35%, #3a0c04 70%, #150402 100%); }
  .authority { background: radial-gradient(circle at 50% 40%, #c79a3e 0%, #6b3d12 30%, #2a0904 60%, #230703 100%); }
  .healing { background: linear-gradient(180deg, #6a5a55 0%, #b58a5a 45%, #f2b45a 70%, #3b2418 100%); }
  .publisher {
    position: absolute;
    left: 106px;
    top: 1008px;
    font-family: "Montserrat", sans-serif;
    font-weight: 500;
    font-size: 25px;
    color: var(--gold-text);
  }
  .author {
    position: absolute;
    left: 240px;
    top: 1040px;
    font-family: "Great Vibes", cursive;
    font-size: 58px;
    color: var(--gold-text);
    white-space: nowrap;
  }
</style>
</head>
<body>
<div class="cover">
  <svg class="cover-lines" width="894" height="1140" viewBox="0 0 894 1140">
    <g fill="none" stroke="var(--line)" stroke-width="2.5">
      <rect x="82" y="110" width="764" height="883"/>
      <line x1="0" y1="150" x2="100" y2="150"/>
      <line x1="0" y1="168" x2="100" y2="168"/>
      <line x1="0" y1="187" x2="100" y2="187"/>
      <line x1="864" y1="973" x2="864" y2="1140"/>
      <line x1="873" y1="973" x2="873" y2="1140"/>
      <line x1="882" y1="973" x2="882" y2="1140"/>
      <line x1="842" y1="973" x2="882" y2="973"/>
    </g>
  </svg>

  <div class="ministry-mark mark-initials">LTM</div>
  <div class="ministry-mark mark-name">LORNA TEBBIT MINISTRIES</div>

  <div class="title-block"></div>
  <div class="split title-script on-tan">Fellowship</div>
  <div class="split title-script on-brown">Fellowship</div>
  <div class="title-main">WORKSHOP 202</div>

  <div class="split tagline on-tan">A LEARN AND DO WORKSHOP WITH<br>LORNA TEBBIT MINISTRIES</div>
  <div class="split tagline on-brown">A LEARN AND DO WORKSHOP WITH<br>LORNA TEBBIT MINISTRIES</div>
  <div class="split sessions on-tan">SESSIONS</div>
  <div class="split sessions on-brown">SESSIONS</div>

  <div class="session-strip"></div>
  <div class="session-grid">
    <div class="session evangelism" role="img" aria-label="Open hands raised toward a glowing cross against a bright sky">
      <span class="session-label label-left">EVANGELISM</span>
    </div>
    <div class="session tongues" role="img" aria-label="A white dove in front of a flaming heart">
      <span class="session-label label-right">PRAYING IN TONGUES</span>
    </div>
    <div class="session authority" role="img" aria-label="A gold officer badge on a dark background">
      <span class="session-label label-left">AUTHORITY OF THE BELIEVER</span>
    </div>
    <div class="session healing" role="img" aria-label="Silhouette of a man standing with arms raised beside an empty wheelchair at sunset">
      <span class="session-label label-right">HEALING</span>
    </div>
  </div>

  <div class="publisher">LORNA TEBBIT MINISTRIES</div>
  <div class="author">Autor: Lorna Tebbit</div>
</div>
</body>
</html>
```